International service dog training school needs web design

We need to upgrade our website. The website is https://brevantmoor.example/
We help trainers and service dog programs learn how to train service dogs with the latest and most ethical training methods. We offer online and in-person coaching services. We would like to see designs that are engaging and communicate professionalism, expertise, and care for the dogs and people we work with. Please also keep the colors already in the logo in the design.

```html
<!DOCTYPE html>
<html lang="en">
<head>
<meta charset="utf-8">
<title>Brevantmoor Center for Assistance Canines</title>
<link href="https://fonts.googleapis.com/css2?family=Roboto:wght@300;400;500;700&display=swap" rel="stylesheet">
<style>
:root{
  --blue:#1a72c2;
  --teal:#0d9c8f;
  --yellow:#ffe000;
  --red:#c8102e;
  --sky:#a8cbe6;
  --sky-soft:#cfe2f1;
  --ink:#1b1b1b;
  --muted:#555;
  --footer:#f5f5f5;
}
*{box-sizing:border-box;margin:0;padding:0}
html,body{width:1200px;height:2429px;overflow:hidden;background:#fff}
body{font-family:'Roboto',sans-serif;color:var(--ink);position:relative}
.abs{position:absolute}
.hero{left:0;top:0;width:1200px;height:390px;background:linear-gradient(180deg,#3d5a3a 0%,#5d7550 45%,#8a9a80 80%,#b9c0b3 100%);overflow:hidden}
.hero-wave{left:0;top:320px;width:1200px;height:75px}
.brand{left:150px;top:24px;display:flex;align-items:center;gap:8px;color:#3aa6d8;font-size:14px;font-weight:500;line-height:1.15;width:200px}
.brand-dot{width:34px;height:34px;border-radius:50%;background:#3aa6d8;flex:none}
.nav{top:36px;left:603px;display:flex;gap:37px;color:#fff;font-size:15px;font-weight:500}
.nav span{white-space:nowrap}
.hero h1{top:100px;left:0;width:1200px;text-align:center;color:#fff;font-weight:400;font-size:42px}
.hero p{top:170px;left:240px;width:720px;text-align:center;color:#fff;font-size:13.5px;font-weight:300;line-height:17px}
.btn-white{background:#fff;color:var(--ink);border-radius:24px;font-size:17px;font-weight:500;display:flex;align-items:center;justify-content:center}
.service-icon{width:144px;height:144px;border-radius:50%;display:flex;align-items:center;justify-content:center}
.service-title{width:300px;text-align:center;font-size:19px;font-weight:400}
.service-text{width:290px;text-align:center;font-size:14.5px;color:var(--muted);line-height:19.5px;font-weight:400}
.btn-outline{border:2px solid var(--red);border-radius:20px;background:#fff;color:var(--ink);font-size:14.5px;display:flex;align-items:center;justify-content:center}
.explore{top:756px;left:0;width:1200px;text-align:center;font-size:36px;font-weight:500}
.card{width:243px;height:369px;background:#fff;box-shadow:0 1px 6px rgba(0,0,0,.25);top:858px}
.card-photo{width:243px;height:158px}
.card h3{position:absolute;left:16px;top:169px;width:220px;font-size:23px;font-weight:400;line-height:27px}
.card p{position:absolute;left:16px;top:234px;width:215px;font-size:13px;color:var(--muted);line-height:16px;font-weight:300}
.card .price{position:absolute;left:16px;font-size:13.5px;color:var(--blue)}
.card-foot{position:absolute;left:0;bottom:0;width:243px;height:30px;border-top:1px solid #ddd;display:flex;align-items:center;justify-content:space-between;padding:0 16px;font-size:10px}
.card-foot a{color:var(--blue);text-decoration:underline}
.hours{display:flex;align-items:center;gap:6px;color:#444}
.coach h2{top:1425px;left:625px;font-size:36px;font-weight:500}
.coach p{top:1488px;left:627px;width:380px;font-size:16px;line-height:20px}
.field{left:628px;width:337px;height:25px;border:1px solid #c8c8c8;font-size:13px;color:#999;padding:5px 11px}
.book{left:0;top:1852px;width:1200px;height:301px;background:var(--blue)}
.book-photo{left:0;top:1852px;width:650px;height:301px;background:linear-gradient(90deg,#4b4a47 0%,#6f6c67 60%,rgba(111,108,103,0) 100%)}
.badge{left:503px;top:1912px;width:176px;height:176px;border-radius:50%;background:var(--red);border:2px solid var(--yellow);color:#fff;text-align:center}
.book h2{position:absolute;left:720px;top:64px;color:#fff;font-size:31px;font-weight:500;line-height:40px}
.book .sub{position:absolute;left:720px;top:147px;color:#fff;font-size:12.5px;line-height:14px;width:280px}
.footer{left:0;top:2153px;width:1200px;height:276px;background:var(--footer)}
.f-head{font-size:10px;font-weight:500;color:#222}
.f-small{font-size:9px;color:#222;line-height:19.5px}
</style>
</head>
<body>

<section class="abs hero" role="img" aria-label="Photo of a fluffy dog running through a green field">
  <svg class="abs hero-wave" viewBox="0 0 1200 75" preserveAspectRatio="none"><path d="M0 30 C200 -5 380 5 600 20 C820 35 1000 -10 1200 35 L1200 75 L0 75Z" fill="#fff"/></svg>
</section>
<div class="abs brand"><span class="brand-dot"></span><span>Maren Solvik Ph.D.<br>Brevantmoor Center</span></div>
<nav class="abs nav"><span>Home</span><span>Courses ⌄</span><span>Our Service ⌄</span><span>About Us</span><span>Blog</span></nav>
<div class="hero"></div>
<h1 class="abs" style="top:100px;left:0;width:1200px;text-align:center;color:#fff;font-weight:400;font-size:42px">Coaching for Service Dog Professionals</h1>
<p class="abs" style="top:170px;left:240px;width:720px;text-align:center;color:#fff;font-size:13.5px;font-weight:300;line-height:17px">The Brevantmoor Center for Assistance Canines was founded by Maren Solvik Ph.D. in response to demand for coaching from dog trainers, medical professionals, and service dog programs.</p>
<div class="abs btn-white" style="left:503px;top:223px;width:194px;height:44px">Learn More --&gt;</div>

<!-- blue blob behind cards -->
<svg class="abs" style="left:700px;top:660px" width="500" height="600" viewBox="0 0 500 600"><path d="M500 5 C420 -10 330 40 280 130 C230 220 150 260 100 350 C40 460 80 580 230 590 C350 598 430 560 500 550Z" fill="var(--sky)"/><path d="M500 0 C460 10 420 20 400 40 L500 30Z" fill="var(--sky-soft)"/></svg>

<div class="abs service-icon" style="left:202px;top:361px;background:var(--blue)">
  <svg width="70" height="70" viewBox="0 0 70 70" fill="none" stroke="#fff" stroke-width="2.5"><rect x="6" y="8" width="58" height="40" rx="3"/><path d="M28 48v8h14v-8M22 60h26M22 28l13-7 13 7-13 7z M27 31v6c5 3 11 3 16 0v-6"/></svg>
</div>
<div class="abs service-icon" style="left:528px;top:361px;background:var(--teal)">
  <svg width="74" height="70" viewBox="0 0 74 70" fill="none" stroke="#fff" stroke-width="2.5"><rect x="4" y="6" width="30" height="20" rx="2"/><rect x="38" y="14" width="30" height="20" rx="2"/><circle cx="24" cy="40" r="6"/><circle cx="52" cy="46" r="6"/><path d="M12 62c0-8 6-12 12-12s12 4 12 12M40 66c0-6 5-10 12-10s12 4 12 10M6 62h34"/></svg>
</div>
<div class="abs service-icon" style="left:854px;top:361px;background:var(--yellow)">
  <svg width="70" height="70" viewBox="0 0 70 70" fill="none" stroke="#fff" stroke-width="2.5"><rect x="22" y="6" width="42" height="30" rx="2"/><circle cx="14" cy="14" r="5"/><path d="M8 64V26h12l12-6M20 40v24M36 40a5 5 0 1 0 0.1 0M52 40a5 5 0 1 0 0.1 0M28 64c0-8 4-12 8-12s8 4 8 12M44 64c0-8 4-12 8-12s8 4 8 12"/></svg>
</div>

<div class="abs service-title" style="left:124px;top:528px">Trainers Courses</div>
<div class="abs service-title" style="left:450px;top:528px">Individualized consulting</div>
<div class="abs service-title" style="left:776px;top:528px">Presentations and Seminars</div>
<div class="abs service-text" style="left:129px;top:569px">The courses offered by the Brevantmoor Center for Assistance Canines (BCAC) are live, interactive and hands on.&nbsp; They are not pre-recorded</div>
<div class="abs service-text" style="left:455px;top:569px">Lorem ipsum dolor sit amet, consectetur adipiscing elit, sed do eiusmod tempor incididunt ut labore et dolore magna aliqua. Quis ipsum suspendisse ultrices</div>
<div class="abs service-text" style="left:781px;top:569px">Lorem ipsum dolor sit amet, consectetur adipiscing elit, sed do eiusmod tempor incididunt ut labore et dolore magna aliqua. Quis ipsum suspendisse ultrices</div>
<div class="abs btn-outline" style="left:199px;top:666px;width:150px;height:37px">Learn More --&gt;</div>
<div class="abs btn-outline" style="left:525px;top:666px;width:150px;height:37px">Learn More --&gt;</div>
<div class="abs btn-outline" style="left:854px;top:666px;width:150px;height:37px">Learn More --&gt;</div>

<h2 class="abs explore">Explore content developed by Maren Solvik</h2>

<svg class="abs" style="left:148px;top:1020px" width="26" height="44" viewBox="0 0 26 44"><path d="M22 2 3 22l19 20" fill="none" stroke="#333" stroke-width="1.5"/></svg>
<svg class="abs" style="left:1026px;top:1020px" width="26" height="44" viewBox="0 0 26 44"><path d="M4 2l19 20L4 42" fill="none" stroke="#333" stroke-width="1.5"/></svg>

<article class="abs card" style="left:200px">
  <div class="card-photo" role="img" aria-label="Photo of a golden retriever being groomed by a trainer" style="background:linear-gradient(135deg,#e9e3dc,#c9a676)"></div>
  <h3>All You Need - Full Carriculum</h3>
  <p>Everything you will need to get started as a service dog trainer specialized in medical detection</p>
  <div class="price" style="top:293px">$1250.00</div>
  <div class="card-foot"><a>Learn More</a><span class="hours"><svg width="11" height="11" viewBox="0 0 11 11" fill="none" stroke="#444"><circle cx="5.5" cy="5.5" r="4.7"/><path d="M5.5 3v2.7l1.8 1"/></svg>38 hours</span></div>
</article>
<article class="abs card" style="left:478px">
  <div class="card-photo" role="img" aria-label="Photo of a tricolour dog lying on a wooden floor with a toy" style="background:linear-gradient(135deg,#8a5a2e,#c98b4f)"></div>
  <h3>Service Dog Candidate Selection</h3>
  <p>Practical learning experience with live project work and examples. suitable for trainers experienced in reading dog behavior</p>
  <div class="price" style="top:309px">$1500.00</div>
  <div class="card-foot"><a>Learn More</a><span class="hours"><svg width="11" height="11" viewBox="0 0 11 11" fill="none" stroke="#444"><circle cx="5.5" cy="5.5" r="4.7"/><path d="M5.5 3v2.7l1.8 1"/></svg>10 hours</span></div>
</article>
<article class="abs card" style="left:756px">
  <div class="card-photo" role="img" aria-label="Photo of a curly black and white service dog wearing a vest" style="background:linear-gradient(135deg,#6d6d6d,#b5b5b5)"></div>
  <h3>Service Dog Training &amp; Assessments</h3>
  <p>complete system to train service dogs along with all the basic behaviors for any service dog</p>
  <div class="price" style="top:293px">$1250.00</div>
  <div class="card-foot"><a>Learn More</a><span class="hours"><svg width="11" height="11" viewBox="0 0 11 11" fill="none" stroke="#444"><circle cx="5.5" cy="5.5" r="4.7"/><path d="M5.5 3v2.7l1.8 1"/></svg>38 hours</span></div>
</article>

<svg class="abs" style="left:0;top:1310px" width="560" height="543" viewBox="0 0 560 543"><path d="M0 30 C120 40 200 0 300 0 C420 0 540 60 538 150 C535 280 430 420 330 490 C290 520 250 535 220 543 L0 543Z" fill="var(--sky-soft)"/><path d="M0 70 C100 70 180 40 280 40 C400 40 480 110 460 220 C440 330 360 450 240 543 L0 543Z" fill="var(--sky)"/></svg>
<div class="abs" role="img" aria-label="Photo of a sitting yellow labrador retriever" style="left:60px;top:1370px;width:410px;height:420px;border-radius:45% 45% 30% 30%;background:radial-gradient(ellipse at 55% 45%,#d9a560 0%,#c48a45 55%,rgba(196,138,69,0) 72%)"></div>

<h2 class="abs" style="top:1425px;left:625px;font-size:36px;font-weight:500">International Coaching</h2>
<p class="abs" style="top:1488px;left:627px;width:380px;font-size:16px;line-height:20px">Seminars and consulting are provided in English or in French. Maren Solvik Ph.D. will travel to your location and help with your particular needs. Online session also available.</p>
<div class="abs field" style="top:1589px">Your Name</div>
<div class="abs field" style="top:1630px">Your Email</div>
<div class="abs btn-outline" style="left:631px;top:1669px;width:116px;height:37px;font-size:15px">Submit</div>

<section class="abs book">
  <h2>New book from<br>Maren Solvik (Ph.D)</h2>
  <div class="sub">Choosing And Preparing Your Service Dog and Learn How to Succeed in Public Access Work.</div>
  <div class="abs btn-white" style="left:720px;top:193px;width:149px;height:37px;font-size:15px;font-weight:400">Oreder Now --&gt;</div>
</section>
<div class="abs book-photo" role="img" aria-label="Photo of the printed book with a service dog on its cover, lying on a wooden table"></div>
<div class="abs" style="left:212px;top:1872px;width:202px;height:255px;background:linear-gradient(180deg,#f1ede6 0%,#e7dfd2 45%,#9a8a6f 75%,#a8202c 100%)" role="img" aria-label="Book cover with a labrador in a red service vest"></div>
<div class="abs" style="left:590px;top:1852px;width:2px;height:60px;background:#fff"></div>
<div class="abs badge">
  <div style="margin-top:38px;font-size:12px;font-weight:500">Up to</div>
  <div style="font-size:52px;font-weight:500;line-height:56px">15%</div>
  <div style="font-size:8.5px;line-height:10px">Lorem ipsum dolor<br>sadipiscing elit, sed</div>
</div>
<div class="abs" style="left:584px;top:1906px;width:16px;height:16px;border-radius:50%;border:2px solid var(--yellow);background:var(--red)"></div>

<footer class="abs footer">
  <div class="abs" style="left:168px;top:55px;display:flex;align-items:center;gap:8px;font-size:13px;color:#222;line-height:15px"><span style="width:38px;height:38px;border-radius:50%;background:#222;display:block"></span><span>Maren Solvik Ph.D.<br>Brevantmoor Center</span></div>
  <div class="abs" style="left:168px;top:109px;font-size:10px;color:#444">Copyright © 2021&nbsp;&nbsp;&nbsp;&nbsp;All Rights Reserved</div>
  <div class="abs f-head" style="left:463px;top:51px">LINKS</div>
  <div class="abs f-small" style="left:462px;top:75px;line-height:30px">Home<br>Courses<br>Our Service<br>AboutUs<br>Blog</div>
  <div class="abs f-head" style="left:610px;top:51px">CONTACT US</div>
  <div class="abs f-small" style="left:610px;top:85px">418 Larkfield Rd<br>Millbrook IN 46999<br>Phone: 555-010-2840</div>
  <div class="abs" style="left:610px;top:186px;display:flex;gap:17px"><span style="width:22px;height:22px;border-radius:50%;background:#e4e4e4"></span><span style="width:22px;height:22px;border-radius:50%;background:#e4e4e4"></span><span style="width:22px;height:22px;border-radius:50%;background:#e4e4e4"></span><span style="width:22px;height:22px;border-radius:50%;background:#e4e4e4"></span></div>
  <div class="abs f-head" style="left:803px;top:51px">SUBSCRIBE TO OUR NEWSLETTER</div>
  <div class="abs f-small" style="left:803px;top:85px;width:230px;font-size:8.5px">Subscribe to our newsletter to stay up to date with the latest news</div>
  <div class="abs" style="left:803px;top:136px;width:222px;height:26px;border:1px solid #c8c8c8;background:#fff;font-size:13px;color:#999;padding:5px 11px">Enter Your Email</div>
  <div class="abs btn-outline" style="left:801px;top:178px;width:116px;height:37px;font-size:15px">Submit</div>
</footer>

</body>
</html>
```